Brindle Tides Boat Business Website

I would like a website that looks fresh, fun and exciting with great colors and photos of people having fun sailing and power boating. Current web page is www.brindletides.example. I want to be able to change content and photos myself once completed. Also needs to have customized info request forms and access to enrollment forms. Should work across all browsers and platforms including iPad and Mac. I have three product lines...instruction, charters and trips. See also keelhour.example/new-york, and facebook.com/brindletides, /keelhournewyork and /conchlagoonbar.
Updates

Reason: We are reviewing the designs submitted and will provide feedback asap. Thank you.

Industry/Entity Type

Business

Requirements
Must have
• self management/content management
form submissions
color, fun, excitement
links pages
photo pages
Nice to have
• calendar/class scheduling
guest book
visitor uploadable photos

```html
<!DOCTYPE html>
<html lang="en">
<head>
<meta charset="utf-8">
<title>Brindle Tides Charter Co. &amp; Nautical School</title>
<link rel="stylesheet" href="https://fonts.googleapis.com/css2?family=Open+Sans:ital,wght@0,400;0,600;0,700;1,400&family=Ubuntu:wght@400;500&display=swap">
<style>
:root{
  --gold:#f7b52c;
  --gold-light:#fcc94a;
  --gold-dark:#e89c12;
  --navy:#141926;
  --teal:#14807f;
  --blue:#1d8ac7;
  --link:#1e6fa8;
  --text:#555;
  --grey-bg:#ededed;
  --footer-top:#3d3d3d;
  --footer-bottom:#1f1f1f;
}
*{box-sizing:border-box;margin:0;padding:0}
html,body{width:1188px;height:1200px;overflow:hidden;background:#fff}
body{font-family:"Open Sans",Arial,sans-serif;color:var(--text);position:relative}
.wrap{position:absolute;left:0;top:0;width:1188px;height:1200px}

/* header */
.site-header{position:absolute;left:0;top:0;width:1188px;height:133px;background:#fff}
.brand{position:absolute;left:136px;top:24px;display:flex;flex-direction:column;align-items:flex-start}
.brand-row{display:flex;align-items:center;gap:10px}
.brand-dot{width:24px;height:24px;border-radius:50%;background:var(--gold)}
.brand-name{font-family:"Open Sans",Arial,sans-serif;font-weight:600;font-size:28px;color:var(--teal);letter-spacing:.5px;margin-top:8px}
.brand-sub{font-size:11.5px;color:var(--teal);letter-spacing:1.4px;text-transform:uppercase;margin-top:1px}
.upload-btn{position:absolute;left:820px;top:45px;width:238px;height:53px;border-radius:8px;background:linear-gradient(#fcc94a,#f4ad23);display:flex;align-items:center;color:#1a1a1a;font-size:14.5px;font-weight:500;letter-spacing:.2px}
.upload-btn .icon{width:48px;height:100%;display:flex;align-items:center;justify-content:center;border-right:1px solid rgba(0,0,0,.18)}
.upload-btn span{padding-left:14px}

/* navigation */
.main-nav{position:absolute;left:0;top:133px;width:1188px;height:39px;background:var(--navy)}
.main-nav ul{list-style:none;position:absolute;left:133px;top:0;height:39px;display:flex}
.main-nav li{height:39px;line-height:39px;font-size:12.5px;color:#fff;padding:0 16.5px}
.main-nav li.active{background:linear-gradient(#fcc94a,#f2a81e);color:#1a1a1a;margin-top:-6px;height:45px;line-height:51px;padding:0 23px;border-radius:2px 2px 0 0}

/* hero */
.hero{position:absolute;left:0;top:172px;width:1188px;height:358px;background:linear-gradient(180deg,#d9c7a8 0%,#f1cf92 30%,#e9b57a 48%,#8c8578 60%,#5f6466 100%)}
.hero-photo{position:absolute;inset:0;background:linear-gradient(90deg,rgba(40,45,55,.45) 0%,rgba(120,110,100,.15) 45%,rgba(0,0,0,0) 70%)}
.enroll{position:absolute;left:780px;top:49px;width:278px;height:309px;background:rgba(38,38,38,.78);border-radius:3px 3px 0 0;padding:18px 18px 0}
.enroll h2{font-family:"Open Sans",Arial,sans-serif;font-weight:600;font-size:19px;color:#fff;letter-spacing:.3px;margin-bottom:14px}
.field{width:243px;height:27px;background:#fff;border:1px solid #d8d8d8;border-radius:2px;font-size:9.5px;font-style:italic;color:#666;padding:6px 10px;margin-bottom:10px}
.field.area{height:63px}
.submit{position:absolute;right:18px;top:216px;width:87px;height:31px;background:linear-gradient(#fcc94a,#f0a51b);border-radius:2px;font-weight:600;font-size:14.5px;color:#1a1a1a;text-align:center;line-height:31px}

/* gallery */
.gallery-band{position:absolute;left:0;top:530px;width:1188px;height:330px;background:var(--grey-bg)}
.gallery-tab{position:absolute;left:124px;top:10px;width:109px;height:43px;background:linear-gradient(#fcc94a,#f2a81e);border-radius:2px 2px 0 0;color:#1a1a1a;font-size:13px;font-weight:500;text-align:center;line-height:45px}
.more-link{position:absolute;right:130px;top:27px;font-size:13px;color:var(--blue)}
.more-link b{color:#222;margin-right:8px;font-size:12px}
.gallery-box{position:absolute;left:124px;top:52px;width:940px;height:270px;background:#fff;border-top:2px solid var(--gold)}
.nav-arrow{position:absolute;top:110px;width:42px;height:72px;background:var(--grey-bg);display:flex;align-items:center;justify-content:center}
.nav-arrow.prev{left:0;border-radius:0 36px 36px 0}
.nav-arrow.next{right:-10px;border-radius:36px 0 0 36px}
.card{position:absolute;top:24px;width:192px}
.card .photo{width:192px;height:146px}
.card h3{font-weight:400;font-size:12px;color:var(--link);margin-top:14px}
.card p{font-size:10px;color:#444;line-height:13px;margin-top:4px;width:150px}
.card .go{font-size:10.5px;color:var(--link);margin-top:8px;display:flex;align-items:center;gap:10px}

/* lower content */
.calendar{position:absolute;left:131px;top:894px;width:216px;height:216px;background:#fff;border:1px solid #ddd;box-shadow:0 10px 12px -6px rgba(0,0,0,.35)}
.cal-head{height:32px;background:linear-gradient(#fbc24a,#f3a929);display:flex;align-items:center;justify-content:space-between;font-family:Ubuntu,Arial,sans-serif;font-size:16px;color:#222;letter-spacing:1px}
.cal-head .arrow{width:22px;height:32px;background:rgba(0,0,0,.07);display:flex;align-items:center;justify-content:center}
.cal-grid{display:grid;grid-template-columns:repeat(7,1fr)}
.cal-grid .dow{font-size:9.5px;color:#777;text-align:center;height:26px;line-height:26px}
.cal-grid .day{font-family:Ubuntu,Arial,sans-serif;font-size:14px;color:#222;text-align:center;height:31px;line-height:31px;border-right:1px solid #e3e3e3;border-top:1px solid #e3e3e3}
.cal-grid .day:nth-child(7n){border-right:none}
.cal-grid .day.muted{background:#ececec;color:#999}
.cal-grid .day.today{background:var(--gold);color:#222}
.feature{position:absolute;top:894px;width:210px}
.feature .frame{width:210px;height:140px;border:1px solid #e1e1e1;border-radius:3px;padding:6px}
.feature .photo{width:100%;height:100%}
.feature h3{font-weight:400;font-size:17px;color:var(--blue);margin-top:13px;padding-left:2px}
.feature p{font-size:12px;color:#666;line-height:17px;margin-top:9px;padding-left:2px}

/* footer */
.site-footer{position:absolute;left:0;top:1150px;width:1188px;height:50px;background:linear-gradient(var(--footer-top),var(--footer-bottom))}
.site-footer p{position:absolute;left:133px;top:17px;font-size:11px;color:#fff}
.social{position:absolute;right:128px;top:12px;display:flex;gap:9px}
.social span{width:23px;height:23px;border-radius:50%;display:block}
</style>
</head>
<body>
<div class="wrap">

<header class="site-header">
  <div class="brand">
    <div class="brand-row"><span class="brand-dot"></span><span class="brand-name">Brindle Tides</span></div>
    <span class="brand-sub">Charter Co. &amp; Nautical School</span>
  </div>
  <a class="upload-btn">
    <div class="icon">
      <svg width="22" height="20" viewBox="0 0 22 20"><rect x="5" y="1" width="16" height="14" fill="none" stroke="#1a1a1a" stroke-width="2"/><rect x="1" y="5" width="16" height="14" fill="#1a1a1a"/><path d="M3 17l4-5 3 3 3-4 3 6z" fill="#f7b52c"/></svg>
    </div>
    <span>UPLOAD YOUR PHOTOS</span>
  </a>
</header>

<nav class="main-nav">
  <ul>
    <li class="active">Home</li>
    <li>Nautical School</li>
    <li>Charter Sailing</li>
    <li>Charter Power</li>
    <li>Our Captains</li>
    <li>Adventure Travel</li>
    <li>Sign Up Today</li>
    <li>Contact Us</li>
    <li>Sitemap</li>
  </ul>
</nav>

<section class="hero">
  <div class="hero-photo" role="img" aria-label="Sailboat deck with winch and coiled blue rope at sunset over the sea"></div>
  <form class="enroll">
    <h2>ENROLL NOW</h2>
    <div class="field">Enter your name...</div>
    <div class="field">Enter your email...</div>
    <div class="field area">Enter your description...</div>
    <div class="submit">Submit</div>
  </form>
</section>

<section class="gallery-band">
  <div class="gallery-tab">Photo Gallery</div>
  <div class="more-link"><b>››</b>More new Galleries</div>
  <div class="gallery-box">
    <div class="nav-arrow prev"><svg width="16" height="20" viewBox="0 0 16 20"><path d="M12 2L4 10l8 8" fill="none" stroke="#1d8ac7" stroke-width="4"/></svg></div>
    <div class="nav-arrow next"><svg width="16" height="20" viewBox="0 0 16 20"><path d="M4 2l8 8-8 8" fill="none" stroke="#1d8ac7" stroke-width="4"/></svg></div>

    <div class="card" style="left:50px">
      <div class="photo" role="img" aria-label="Group of friends waving from a heeling sailboat" style="background:linear-gradient(180deg,#6f93c2 0%,#a9bfd8 55%,#2b2f36 100%)"></div>
      <h3>Lorem Ipsum</h3><p>Lorem Ipsum Dolor Sit amet and type</p>
      <div class="go">Click to go <svg width="12" height="9" viewBox="0 0 12 9"><path d="M1 1l3.5 3.5L1 8M6 1l3.5 3.5L6 8" fill="none" stroke="#f7b52c" stroke-width="2"/></svg></div>
    </div>
    <div class="card" style="left:267px">
      <div class="photo" role="img" aria-label="Sailors at the helm of a boat on a sunny day" style="background:linear-gradient(180deg,#4f86c9 0%,#8fb1d6 45%,#6b6f78 100%)"></div>
      <h3>Lorem Ipsum</h3><p>Lorem Ipsum Dolor Sit amet and type</p>
      <div class="go">Click to go <svg width="12" height="9" viewBox="0 0 12 9"><path d="M1 1l3.5 3.5L1 8M6 1l3.5 3.5L6 8" fill="none" stroke="#f7b52c" stroke-width="2"/></svg></div>
    </div>
    <div class="card" style="left:484px">
      <div class="photo" role="img" aria-label="Passengers in life jackets on a speeding inflatable boat" style="background:linear-gradient(180deg,#b8c8de 0%,#7f95b6 45%,#2f4a8a 75%,#3d5f9c 100%)"></div>
      <h3>Lorem Ipsum</h3><p>Lorem Ipsum Dolor Sit amet and type</p>
      <div class="go">Click to go <svg width="12" height="9" viewBox="0 0 12 9"><path d="M1 1l3.5 3.5L1 8M6 1l3.5 3.5L6 8" fill="none" stroke="#f7b52c" stroke-width="2"/></svg></div>
    </div>
    <div class="card" style="left:702px">
      <div class="photo" role="img" aria-label="Family fishing from the stern of a white motorboat" style="background:linear-gradient(180deg,#9fb7cf 0%,#e4e8ec 50%,#4b7aa6 100%)"></div>
      <h3>Lorem Ipsum</h3><p>Lorem Ipsum Dolor Sit amet and type</p>
      <div class="go">Click to go <svg width="12" height="9" viewBox="0 0 12 9"><path d="M1 1l3.5 3.5L1 8M6 1l3.5 3.5L6 8" fill="none" stroke="#f7b52c" stroke-width="2"/></svg></div>
    </div>
  </div>
</section>

<aside class="calendar">
  <div class="cal-head">
    <div class="arrow"><svg width="8" height="12" viewBox="0 0 8 12"><path d="M6 1L1.5 6 6 11" fill="none" stroke="#fff" stroke-width="2"/></svg></div>
    <span>APRIL 2013</span>
    <div class="arrow"><svg width="8" height="12" viewBox="0 0 8 12"><path d="M2 1l4.5 5L2 11" fill="none" stroke="#fff" stroke-width="2"/></svg></div>
  </div>
  <div class="cal-grid">
    <div class="dow">SUN</div><div class="dow">MON</div><div class="dow">TUE</div><div class="dow">WED</div><div class="dow">THU</div><div class="dow">FRI</div><div class="dow">SAT</div>
    <div class="day"></div><div class="day">1</div><div class="day">2</div><div class="day">3</div><div class="day">4</div><div class="day">5</div><div class="day">6</div>
    <div class="day">7</div><div class="day">8</div><div class="day">9</div><div class="day">10</div><div class="day">11</div><div class="day muted">12</div><div class="day">13</div>
    <div class="day">14</div><div class="day">15</div><div class="day today">16</div><div class="day">17</div><div class="day">18</div><div class="day">19</div><div class="day">20</div>
    <div class="day">21</div><div class="day">22</div><div class="day">23</div><div class="day">24</div><div class="day">25</div><div class="day">26</div><div class="day">27</div>
    <div class="day">28</div><div class="day">29</div><div class="day">30</div><div class="day">31</div><div class="day"></div><div class="day"></div><div class="day"></div>
  </div>
</aside>

<article class="feature" style="left:387px">
  <div class="frame"><div class="photo" role="img" aria-label="Students in a small turquoise sailing dinghy" style="background:linear-gradient(180deg,#5f9fb8 0%,#43b5c4 60%,#2f8fa0 100%)"></div></div>
  <h3>Instructions</h3>
  <p>Lorem Ipsum is simply dummy text of the printing and typesetting .</p>
</article>
<article class="feature" style="left:619px">
  <div class="frame"><div class="photo" role="img" aria-label="Bow of a sailboat on open blue water with a distant sail" style="background:linear-gradient(180deg,#7fb0df 0%,#b9d5ee 40%,#1d4f8f 55%,#14447f 100%)"></div></div>
  <h3>Charters</h3>
  <p>Lorem Ipsum is simply dummy text of the printing and typesetting .</p>
</article>
<article class="feature" style="left:852px">
  <div class="frame"><div class="photo" role="img" aria-label="Motor yacht cruising at speed across dark blue sea" style="background:linear-gradient(160deg,#2d4f6f 0%,#3b6584 45%,#c9d3da 60%,#2a4d6c 100%)"></div></div>
  <h3>Trips</h3>
  <p>Lorem Ipsum is simply dummy text of the printing and typesetting .</p>
</article>

<footer class="site-footer">
  <p>©copyright 2013. Brindle Tides Charter Co. and Nautical School. All rights reserved.</p>
  <div class="social" aria-label="Social links">
    <span style="background:#2aa3d9"></span>
    <span style="background:#3a66b0"></span>
    <span style="background:#6a6a6a"></span>
    <span style="background:#1b7dc0"></span>
  </div>
</footer>

</div>
</body>
</html>
```